Business Card Design

I already have a company logo for my company. I have a logo for the manufacturer we represent. I want a professional business card design.

```html
<!DOCTYPE html>
<html lang="en">
<head>
<meta charset="utf-8">
<title>Signal Guard LLC – Business Card</title>
<link rel="stylesheet" href="https://fonts.googleapis.com/css2?family=Poppins:wght@400;700&display=swap">
<style>
  :root {
    --backdrop: #ababab;
    --card-white: #ffffff;
    --card-black: #000000;
    --brand-red: #e31e24;
    --ink: #1a1a1a;
    --ink-soft: #333333;
    --rule: #c8c8c8;
    --gold: #d9a400;
  }
  * { margin: 0; padding: 0; box-sizing: border-box; }
  html, body {
    width: 1093px; height: 1200px; overflow: hidden;
    background: var(--backdrop);
    font-family: "Poppins", sans-serif;
  }
  .canvas { position: relative; width: 1093px; height: 1200px; }

  .card { position: absolute; left: 265px; border-radius: 26px; overflow: hidden; }
  .card--front { top: 226px; width: 577px; height: 356px; background: var(--card-white); }
  .card--back  { top: 621px; width: 583px; height: 360px; background: var(--card-black); }

  .brand {
    position: absolute; display: flex; flex-direction: column; align-items: center;
    font-weight: 700; color: var(--brand-red); text-align: center; line-height: 1.05;
  }
  .brand__mark { width: 26px; height: 26px; background: var(--brand-red); margin-bottom: 12px; }
  .card--front .brand { left: 47px; top: 96px; width: 210px; font-size: 30px; }
  .card--back .brand { left: 0; top: 118px; width: 583px; font-size: 42px; }
  .card--back .brand__mark { width: 32px; height: 32px; }
  .brand__suffix { font-size: 0.5em; margin-top: 6px; }

  .divider {
    position: absolute; left: 288px; top: 74px; width: 1px; height: 209px; background: var(--rule);
  }

  .contact { position: absolute; left: 311px; top: 88px; color: var(--ink); }
  .contact__name { font-size: 23px; font-weight: 700; color: var(--brand-red); line-height: 1.1; }
  .contact__title { font-size: 17px; color: var(--ink-soft); line-height: 1.2; margin-bottom: 14px; }
  .contact__list { list-style: none; }
  .contact__item { display: flex; align-items: center; font-size: 17px; line-height: 21px; }
  .contact__icon { width: 15px; height: 15px; margin-right: 8px; flex: none; }
  .contact__accent { color: var(--brand-red); }
  .contact__address { font-size: 17px; line-height: 21px; margin-top: 13px; }
</style>
</head>
<body>
<main class="canvas">
  <section class="card card--front" aria-label="Business card front">
    <div class="brand">
      <span class="brand__mark"></span>
      <span>SIGNAL GUARD</span>
      <span class="brand__suffix">LLC</span>
    </div>
    <div class="divider"></div>
    <div class="contact">
      <p class="contact__name">DANIEL HARPER</p>
      <p class="contact__title">Managing Director</p>
      <ul class="contact__list">
        <li class="contact__item">
          <svg class="contact__icon" viewBox="0 0 16 16" aria-hidden="true"><path fill="none" stroke="#e31e24" stroke-width="1.8" d="M4 1.5l2.5 3-1.5 2c1 2 2.5 3.5 4.5 4.5l2-1.5 3 2.5-1.5 2.5C7 15.5 0.5 9 1.5 3z"/></svg>
          044-987 654 321
        </li>
        <li class="contact__item">
          <svg class="contact__icon" viewBox="0 0 16 16" aria-hidden="true"><rect x="0.5" y="3" width="15" height="10" fill="#e31e24"/><path d="M0.5 3.5L8 9l7.5-5.5" fill="none" stroke="#fff" stroke-width="1.2"/></svg>
          hello@signalguard.com
        </li>
        <li class="contact__item">
          <svg class="contact__icon" viewBox="0 0 16 16" aria-hidden="true"><g fill="none" stroke="#e31e24" stroke-width="1.3"><circle cx="8" cy="8" r="7"/><ellipse cx="8" cy="8" rx="3" ry="7"/><path d="M1 8h14M2 4.5h12M2 11.5h12"/></g></svg>
          <span>www.<span class="contact__accent">signalguard</span>.com</span>
        </li>
      </ul>
      <p class="contact__address">421, Address line goes here<br>45452,Country Name</p>
    </div>
  </section>

  <section class="card card--back" aria-label="Business card back">
    <div class="brand">
      <span class="brand__mark"></span>
      <span>SIGNAL GUARD</span>
      <span class="brand__suffix">LLC</span>
    </div>
  </section>
</main>
</body>
</html>
```